Header Design

I would like a new header design for my website - www.nestmarla.com.

I am a Realtor and the header should reflect that and complement the theme.

The attached logo needs to be included and the information that is already there. Also, the colors need to match.

Marla Quinby
Connecting you to the Los Angeles real estate scene.

Industry/Entity Type

Realtor

```html
<!DOCTYPE html>
<html lang="en">
<head>
<meta charset="utf-8">
<title>Marla Quinby – Los Angeles Real Estate</title>
<link rel="stylesheet" href="https://fonts.googleapis.com/css2?family=Questrial&family=Arimo:wght@400;700&display=swap">
<style>
:root{
  --plum:#3a2038;
  --plum-deep:#2f1a2d;
  --page:#e6e4e6;
  --panel:#ffffff;
  --line:#d4d4d4;
  --ink:#222222;
  --muted:#555555;
  --sky-top:#a9867f;
  --sky-bottom:#d69a6a;
  --night-top:#2c3157;
  --night-bottom:#1b1826;
  --action:#2a7de1;
  --search-btn:#2d2d2d;
  --rss:#f08a24;
  --badge:#d8453b;
}
*{box-sizing:border-box;margin:0;padding:0}
html,body{width:1200px;height:724px;overflow:hidden}
body{background:var(--page);font-family:"Arimo",Arial,sans-serif;color:var(--ink);position:relative}
.abs{position:absolute}

/* header */
.site-header{position:absolute;left:0;top:0;width:1200px;height:171px;background:var(--plum)}
.brand{left:60px;top:56px;display:flex;align-items:center;gap:8px;color:#fff;font-family:"Questrial",sans-serif;font-size:17px;line-height:20px;width:130px}
.brand-square{width:14px;height:14px;background:#fff;flex:none}
.banner{left:197px;top:6px;width:806px;height:124px;background:linear-gradient(180deg,var(--sky-top),var(--sky-bottom) 60%,#8a5d4c)}
.banner-name{position:absolute;left:0;right:0;top:22px;text-align:center;color:#fff;font-family:"Questrial",sans-serif;font-size:36px}
.banner-strip{position:absolute;left:0;bottom:0;width:100%;height:40px;background:rgba(40,22,30,.78);color:#fff;font-family:"Questrial",sans-serif;font-size:15px;text-align:center;line-height:40px;letter-spacing:.3px}
.hotline{right:20px;top:20px;text-align:right;color:#fff;font-family:"Questrial",sans-serif;font-size:23px;line-height:33px}
.main-nav{position:absolute;left:0;top:136px;width:1200px;display:flex;justify-content:space-between;padding:0 16px 0 24px;font-family:"Questrial",sans-serif;font-size:17.5px;color:#fff}

/* content */
.content-panel{left:20px;top:183px;width:753px;height:541px;background:var(--panel);border:1px solid var(--line)}
.slider{left:36px;top:197px;width:719px;height:372px;background:linear-gradient(180deg,var(--night-top),var(--night-bottom) 55%,#3a2a2c)}
.slider-caption{left:43px;top:533px;width:204px;height:31px;background:rgba(30,30,30,.8);color:#fff;font-size:15px;line-height:31px;padding-left:10px}
.slider-arrow{top:366px}
.dots{left:324px;top:579px;display:flex;gap:10px}
.dots span{width:10px;height:10px;border-radius:50%;background:#c8c8c8}
.dots span:first-child{background:#555}
.section-bar{height:27px;background:var(--plum);color:#fff;font-weight:700;font-size:13px;line-height:27px;padding-left:10px;text-transform:uppercase}
.news-bar{left:30px;top:615px;width:731px}
.article-thumb{left:36px;top:657px;width:191px;height:67px;background:linear-gradient(180deg,#7ea6d6,#c7d9ee)}
.article{left:240px;top:656px;width:515px;font-size:15px;line-height:22px;color:var(--muted)}
.article h2{font-size:15px;color:var(--ink);margin-bottom:2px}

/* sidebar */
.side-panel{background:var(--panel);border:1px solid var(--line);left:786px;width:384px}
.search-field{left:798px;top:198px;width:288px;height:28px;border:1px solid #cfcfcf;font-size:13px;line-height:26px;padding-left:7px;color:#444;background:#fff}
.search-btn{left:1086px;top:198px;width:67px;height:28px;background:var(--search-btn);color:#fff;font-size:13px;line-height:28px;text-align:center}
.rss{left:900px;top:257px;width:36px;height:36px;background:var(--rss);border-radius:5px}
.plus-badge{left:1039px;top:258px;width:47px;height:28px;border:1px solid #ccc;border-radius:3px;background:#fafafa}
.plus-badge i{position:absolute;left:14px;top:6px;width:16px;height:16px;background:var(--badge);border-radius:3px}
.plus-count{left:1092px;top:258px;width:42px;height:28px;border:1px solid #ccc;border-radius:3px;font-size:14px;line-height:26px;text-align:center;color:#666;background:#fff}
.quick-bar{left:798px;top:325px;width:372px;font-size:12.5px}
.group-title{left:847px;width:281px;font-size:20px;border-bottom:1px solid #333;padding-bottom:2px}
.field-label{left:847px;font-size:12px;color:#444}
.select{height:32px;border:1px solid #aaa;background:#fff;font-size:14px;line-height:30px;padding-left:8px}
.select svg{position:absolute;right:6px;top:8px}
.dash{left:982px;top:610px;font-size:14px}
.search-props{left:914px;top:660px;width:210px;height:38px;background:var(--action);border:1px solid #1b5fb3;color:#fff;font-weight:700;font-size:14px;line-height:36px;text-align:center}
</style>
</head>
<body>
<header class="site-header">
  <div class="abs brand"><span class="brand-square"></span><span>Marla Quinby</span></div>
  <div class="abs banner" role="img" aria-label="Los Angeles downtown skyline at dusk">
    <div class="banner-name">Marla Quinby</div>
    <div class="banner-strip">CONNECTING YOU TO THE LOS ANGELES REAL ESTATE SCENE</div>
  </div>
  <div class="abs hotline">Hotline:<br>310.555.0142</div>
  <nav class="main-nav">
    <span>Home</span><span>About Marla</span><span>Home Search Central</span><span>Search By Community</span><span>Buyers</span><span>Sellers</span><span>Renters</span><span>Market Reports</span><span>Contact Me</span>
  </nav>
</header>

<main>
  <div class="abs content-panel"></div>
  <div class="abs slider" role="img" aria-label="Los Angeles city lights at night under a rising moon"></div>
  <svg class="abs slider-arrow" style="left:62px" width="16" height="34" viewBox="0 0 16 34"><path d="M14 2 2 17l12 15" fill="none" stroke="#fff" stroke-opacity=".7" stroke-width="3"/></svg>
  <svg class="abs slider-arrow" style="left:708px" width="16" height="34" viewBox="0 0 16 34"><path d="M2 2l12 15L2 32" fill="none" stroke="#fff" stroke-opacity=".7" stroke-width="3"/></svg>
  <div class="abs slider-caption">Los Angeles Home Search</div>
  <div class="abs dots"><span></span><span></span><span></span><span></span><span></span><span></span><span></span></div>

  <div class="abs section-bar news-bar">Los Angeles Real Estate News and Views</div>
  <div class="abs article-thumb" role="img" aria-label="High-rise condo tower against blue sky"></div>
  <article class="abs article">
    <h2>Century City Condos for Sale 2013 in Review</h2>
    <p>Century City condos have a mix of full service high rise buildings and gated garden complexes with full amenities.&nbsp; Away from the bustle and bustle with</p>
  </article>
</main>

<aside>
  <div class="abs side-panel" style="top:186px;height:50px"></div>
  <div class="abs search-field">Search this website…</div>
  <div class="abs search-btn">SEARCH</div>

  <div class="abs side-panel" style="top:245px;height:50px"></div>
  <div class="abs rss"></div>
  <div class="abs plus-badge"><i></i></div>
  <div class="abs plus-count">339</div>

  <div class="abs side-panel" style="top:305px;height:430px"></div>
  <div class="abs section-bar quick-bar">Find Your Next Home – Quick Search</div>
  <div class="abs group-title" style="top:358px">Location</div>
  <div class="abs field-label" style="top:395px">CITY</div>
  <div class="abs select" style="left:847px;top:423px;width:265px">Any<svg width="16" height="16"><rect x=".5" y=".5" width="15" height="15" fill="#eee" stroke="#888"/><path d="M4 6h8l-4 5z" fill="#222"/></svg></div>
  <div class="abs field-label" style="top:467px">COMMUNITY</div>
  <div class="abs select" style="left:847px;top:495px;width:265px">Any<svg width="16" height="16"><rect x=".5" y=".5" width="15" height="15" fill="#eee" stroke="#888"/><path d="M4 6h8l-4 5z" fill="#222"/></svg></div>
  <div class="abs group-title" style="top:543px">Property</div>
  <div class="abs select" style="left:850px;top:602px;width:127px">$0<svg width="16" height="16"><rect x=".5" y=".5" width="15" height="15" fill="#eee" stroke="#888"/><path d="M4 6h8l-4 5z" fill="#222"/></svg></div>
  <div class="abs dash">-</div>
  <div class="abs select" style="left:994px;top:602px;width:128px">$0<svg width="16" height="16"><rect x=".5" y=".5" width="15" height="15" fill="#eee" stroke="#888"/><path d="M4 6h8l-4 5z" fill="#222"/></svg></div>
  <div class="abs search-props">Search for Properties</div>
</aside>
</body>
</html>
```